Postcard Design for a Church

The postcard is for a church. This will be going to new movers in the area. I would like it to say "Welcome to the Neighborhood!" somewhere on the postcard. You can say something like like "Transitioning to a new community can be very difficult and sometimes overwhelming. Our goal as a church is to assist and help where needed". You can also say something like "if you're looking for a church home and a place where you'll be embraced, we invite you to worship with us and be our special guest". Our Facebook page is Facebook.com/TheHarborHouseTN. Our Twitter is TheHarborHouse. Our website page is www.TheHarborHouseTN.org. You can list the vision of the church which is "Our vision is to save souls, change lives & impact the community". Please list the address of the church being located in the main auditorium of Marrowdale High School. The time is Sundays at 11am. The address is 7385 Kettering Lane, Brambleton, TN 37412. Our colors are purple and gold. You can also say "We're more than a church, we're a family". I would like it to also say something like "Come and Grow With Us!" My name is Pastor Darnell "WT" Okafor. My wife's name is First Lady Lashonda Okafor. I hope all this makes sense and it's not exactly in order, but I would like to see your designs. Thank you.

```html
<!DOCTYPE html>
<html lang="en">
<head>
<meta charset="utf-8">
<title>The Harbor House – Welcome Postcard</title>
<link href="https://fonts.googleapis.com/css2?family=PT+Sans+Narrow:wght@400;700&family=Merriweather:ital,wght@0,700;0,900;1,700&family=Parisienne&display=swap" rel="stylesheet">
<style>
  :root{
    --purple:#4b2170;
    --purple-deep:#3a1659;
    --gold:#b79a55;
    --olive:#a3a544;
    --olive-light:#c5c77a;
    --parchment-light:#f6ead0;
    --parchment:#ead6ae;
    --parchment-dark:#d2b17a;
    --ink:#3b2a3f;
    --white:#ffffff;
    --stage:#e4e4e4;
  }
  *{margin:0;padding:0;box-sizing:border-box}
  html,body{width:1200px;height:1200px;overflow:hidden}
  body{background:var(--stage);position:relative;font-family:"PT Sans Narrow",sans-serif}

  .postcard{position:absolute;left:247px;width:706px;height:546px;overflow:hidden}
  .postcard--front{top:48px;background:radial-gradient(ellipse at 60% 40%,var(--parchment-light) 0%,var(--parchment) 60%,var(--parchment-dark) 100%)}
  .postcard--back{top:622px;background:var(--white)}

  .arcs{position:absolute;inset:0}

  .brand{position:absolute;text-align:center;color:var(--purple)}
  .brand__mark{display:block;margin:0 auto;border-radius:50%;background:var(--purple);border:5px solid var(--gold)}
  .brand__name{display:block;font-family:"PT Sans Narrow",sans-serif;font-weight:700;color:var(--purple);line-height:1;white-space:nowrap}

  .front .brand{left:5px;top:32px;width:200px}
  .front .brand__mark{width:150px;height:150px}
  .front .brand__name{font-size:30px;margin-top:20px}

  .photo{position:absolute;left:34px;top:262px;width:256px;height:284px;
    background:linear-gradient(180deg,#8a6a55 0%,#3a2c2a 55%,#1f1a1c 100%);border-radius:110px 110px 0 0}

  .band-olive{position:absolute;left:0;right:0;top:444px;height:36px;background:linear-gradient(180deg,var(--olive-light),var(--olive))}
  .band-purple{position:absolute;left:0;right:0;top:480px;height:66px;background:linear-gradient(180deg,var(--purple) 0%,var(--purple-deep) 100%)}

  .name-tag{position:absolute;font-family:"Merriweather",serif;font-weight:700;font-style:italic;color:var(--white);font-size:12px;line-height:15px;text-shadow:0 1px 2px rgba(0,0,0,.7)}
  .name-tag--pastor{left:140px;top:360px}
  .name-tag--lady{left:54px;top:452px}

  .welcome{position:absolute;left:260px;width:430px;top:40px;text-align:center;color:var(--purple)}
  .welcome__script{font-family:"Parisienne",cursive;font-size:54px;line-height:60px}
  .welcome__title{font-family:"Merriweather",serif;font-weight:900;font-size:40px;line-height:48px}

  .intro{position:absolute;left:300px;top:184px;width:384px;font-size:16.5px;line-height:25px;color:var(--ink)}

  .tagline{position:absolute;left:380px;top:328px;font-family:"Merriweather",serif;font-weight:900;font-size:18px;line-height:23px;color:var(--purple)}
  .invite{position:absolute;left:380px;top:380px;font-family:"Parisienne",cursive;font-size:26px;line-height:30px;color:var(--purple)}

  .social{position:absolute;right:23px;top:484px;text-align:right;color:var(--white);font-weight:700;font-size:16px;line-height:22px}
  .social span{margin-left:14px}

  .back-parchment{position:absolute;left:0;top:0;width:320px;height:546px;
    border-radius:0 100% 100% 0 / 0 80% 60% 0;
    background:radial-gradient(ellipse at 20% 30%,var(--parchment-light) 0%,var(--parchment) 55%,var(--parchment-dark) 100%);
    -webkit-mask-image:linear-gradient(180deg,#000 60%,transparent 85%);
    mask-image:linear-gradient(180deg,#000 60%,transparent 85%)}
  .back .brand{left:15px;top:36px;width:190px}
  .back .brand__mark{width:130px;height:130px}
  .back .brand__name{font-size:28px;margin-top:14px}

  .vision{position:absolute;left:15px;top:236px;width:190px;text-align:center;font-size:11px;line-height:13px;font-style:italic;color:var(--ink)}

  .info-label{position:absolute;left:0;width:140px;height:14px;padding-left:36px;background:linear-gradient(90deg,var(--olive) 60%,transparent);color:var(--white);font-size:11px;letter-spacing:2px;line-height:14px}
  .info-label--location{top:278px}
  .info-label--time{top:394px}
  .info-block{position:absolute;left:36px;color:var(--ink);font-size:18px;line-height:23px}
  .info-block strong{color:var(--purple);font-weight:700}
  .info-block--location{top:292px}
  .info-block--time{top:410px}
</style>
</head>
<body>

<section class="postcard postcard--front front">
  <svg class="arcs" width="706" height="546" viewBox="0 0 706 546" aria-hidden="true">
    <path d="M120 0 C 40 120, 40 300, 230 430 L 0 430 L 0 0 Z" fill="#e6cf9f" opacity=".55"/>
    <path d="M175 0 C 80 140, 90 320, 300 440" fill="none" stroke="#d9bd88" stroke-width="10" opacity=".7"/>
    <path d="M0 250 C 60 330, 140 380, 300 410 L 706 410 L 706 444 L 0 444 Z" fill="var(--olive-light)" opacity=".5"/>
  </svg>

  <div class="brand">
    <span class="brand__mark"></span>
    <span class="brand__name">The Harbor House</span>
  </div>

  <div class="band-olive"></div>
  <div class="band-purple"></div>

  <div class="photo" role="img" aria-label="Photo of the pastor and first lady standing together"></div>
  <p class="name-tag name-tag--pastor">Pastor<br>Darnell "WT" Okafor</p>
  <p class="name-tag name-tag--lady">First Lady<br>Lashonda Okafor</p>

  <header class="welcome">
    <p class="welcome__script">Welcome to the</p>
    <h1 class="welcome__title">Neighborhood!</h1>
  </header>

  <p class="intro">Transitioning to a new community can be very difficult and sometimes overwhelming. Our goal as a church is to assist and help where needed. If you're looking for a church home and a place where you'll be embraced, we invite you to worship with us and be our special guest.</p>

  <p class="tagline">We're more than a church,<br>we're a family.</p>
  <p class="invite">Come and Grow With Us!</p>

  <div class="social">
    <p>Facebook.com/TheHarborHouseTN</p>
    <p>TheHarborHouse<span>www.TheHarborHouseTN.org</span></p>
  </div>
</section>

<section class="postcard postcard--back back">
  <div class="back-parchment"></div>

  <div class="brand">
    <span class="brand__mark"></span>
    <span class="brand__name">The Harbor House</span>
  </div>

  <p class="vision">"Our vision is to save souls, change lives<br>&amp; impact the community".</p>

  <p class="info-label info-label--location">LOCATION</p>
  <p class="info-block info-block--location"><strong>Main auditorium<br>of Marrowdale High School</strong><br>7385 Kettering Lane,<br>Brambleton, TN 37412</p>

  <p class="info-label info-label--time">TIME</p>
  <p class="info-block info-block--time"><strong>Sundays at 11:00am</strong></p>
</section>

</body>
</html>
```